Create a professional, eye-catching business card design that reflects the values and services of Brookfern Veterinary Hospital. we provide veterinary services and the business card should be a memorable representation of the clinic and align with its branding and mission. our tag line is "Faithful Friends, Devoted Care"
Use clean, modern typography. Prioritize readability and professionalism. We would like to see designs that use the color blue, as in the logo example. the final design should communicate professionalism and care, with attention to detail.

```html
<!DOCTYPE html>
<html lang="en">
<head>
<meta charset="utf-8">
<title>Brookfern Veterinary Hospital – Business Card</title>
<link href="https://fonts.googleapis.com/css2?family=Montserrat:wght@300;400;500;700&display=swap" rel="stylesheet">
<style>
  :root {
    --navy: #1e3264;
    --navy-soft: #243a70;
    --white: #ffffff;
    --stage: #5d5e63;
    --ink: #141a2b;
  }
  * { margin: 0; padding: 0; box-sizing: border-box; }
  html, body { width: 1200px; height: 780px; overflow: hidden; }
  body {
    background: var(--stage);
    font-family: "Montserrat", Arial, sans-serif;
    position: relative;
  }
  .card {
    position: absolute;
    top: 75px;
    width: 360px;
    height: 630px;
    background: var(--white);
    overflow: hidden;
    box-shadow: 0 14px 30px rgba(0,0,0,0.35);
  }
  .card--front { left: 180px; }
  .card--back { left: 660px; }

  /* Front */
  .front-band {
    position: absolute;
    left: 0; width: 100%;
    background: var(--navy);
  }
  .front-band--top { top: 0; height: 200px; }
  .front-band--bottom { bottom: 0; height: 200px; }
  .front-pattern {
    position: absolute; inset: 0;
    background: linear-gradient(160deg, var(--navy-soft), var(--navy));
  }
  .brand {
    position: absolute;
    top: 200px; left: 0; width: 100%; height: 230px;
    display: flex; align-items: center; justify-content: center; gap: 14px;
  }
  .brand-dot {
    width: 46px; height: 46px;
    border: 2px solid var(--navy);
    border-radius: 50%;
  }
  .brand-name {
    color: var(--navy);
    font-weight: 700;
    line-height: 1.05;
  }
  .brand-name .brand-word { display: block; font-size: 34px; letter-spacing: 0.5px; }
  .brand-name .brand-sub { display: block; font-size: 11.5px; letter-spacing: 1.2px; }
  .tagline {
    position: absolute;
    left: 46px; bottom: 70px;
    color: var(--white);
    text-transform: uppercase;
    font-size: 17px;
    line-height: 1.4;
    letter-spacing: 0.3px;
  }
  .tagline-light { display: block; font-weight: 300; }
  .tagline-strong { display: block; font-weight: 700; }

  /* Back */
  .back-art { position: absolute; top: 0; left: 0; width: 360px; height: 420px; }
  .doctor {
    position: absolute;
    top: 34px; right: 30px;
    color: var(--white);
    font-size: 21px;
    font-weight: 700;
    letter-spacing: 0.5px;
  }
  .doctor .credential { font-weight: 400; }
  .contact {
    position: absolute;
    right: 30px; bottom: 40px;
    width: 290px;
    color: var(--ink);
    text-align: right;
    font-size: 13.5px;
    line-height: 1.55;
  }
  .contact-rule { height: 1.5px; background: var(--navy); margin: 8px 0; }
  .contact-line { display: flex; justify-content: flex-end; align-items: center; gap: 8px; }
  .contact-icon { width: 13px; height: 13px; flex: none; }
  .contact-web strong { font-weight: 700; }
</style>
</head>
<body>

  <section class="card card--front" aria-label="Card front">
    <div class="front-band front-band--top">
      <div class="front-pattern" role="img" aria-label="Faint repeating clinic emblem pattern"></div>
    </div>

    <div class="brand">
      <span class="brand-dot" aria-hidden="true"></span>
      <p class="brand-name">
        <span class="brand-word">BROOKFERN</span>
        <span class="brand-sub">VETERINARY HOSPITAL</span>
      </p>
    </div>

    <div class="front-band front-band--bottom">
      <div class="front-pattern" role="img" aria-label="Faint repeating clinic emblem pattern"></div>
      <p class="tagline">
        <span class="tagline-light">Faithful Friends,</span>
        <span class="tagline-strong">Devoted Care</span>
      </p>
    </div>
  </section>

  <section class="card card--back" aria-label="Card back">
    <svg class="back-art" viewBox="0 0 360 420" role="img" aria-label="Illustration of a cat and dog on a hilltop under a gum branch and moon">
      <path d="M0 0 H360 V420 C300 400 250 330 200 285 C150 245 90 220 0 205 Z" fill="var(--navy)"/>
    </svg>

    <p class="doctor">Daniel Marsh, <span class="credential">DVM</span></p>

    <div class="contact">
      <div class="contact-rule"></div>
      <p>12 Fernleigh Road,<br>Brookvale, WA 6090</p>
      <p class="contact-line">(08) 9400 2187
        <svg class="contact-icon" viewBox="0 0 24 24" aria-hidden="true"><path d="M6.6 10.8a15 15 0 0 0 6.6 6.6l2.2-2.2c.3-.3.7-.4 1-.2 1.1.4 2.3.6 3.6.6.6 0 1 .4 1 1V20c0 .6-.4 1-1 1C10.6 21 3 13.4 3 4c0-.6.4-1 1-1h3.5c.6 0 1 .4 1 1 0 1.3.2 2.5.6 3.6.1.3 0 .7-.2 1z" fill="var(--navy)"/></svg>
      </p>
      <div class="contact-rule"></div>
      <p class="contact-line">reception@brookfernvet.com.au
        <svg class="contact-icon" viewBox="0 0 24 24" aria-hidden="true"><rect x="2" y="5" width="20" height="14" fill="var(--navy)"/><path d="M2 5l10 8 10-8" fill="none" stroke="var(--white)" stroke-width="1.6"/></svg>
      </p>
      <p class="contact-web">www.<strong>brookfernvet</strong>.com.au</p>
    </div>
  </section>

</body>
</html>
```